Quorvex.com.au - Managed online product sales programs, software platform and apps.

1. Sales & Distribution.We sell your products. On multiple websites, or to major retailers and independents, Clearance and job lots. We managed sales of products via our existing retail channels or a combination of .our channels and clients channels.
2. Software Applications. Use our platforms to manage the products, sales, tracking , customer service and more. Download our apps. Use of our platforms, like www.plindar.com , or one of our many webstores, like vornibuy.com.au . Use of our apps for product management, sales, tracking and customer service notifications
3. Marketing .Omni channel Programs Online Marketing and SEO optimisation, to maximise your exposure. Marketing - SEO and strategies to increase sales and broaden exposure.

4. Consulting. Special projects and Custom work from advise, to software development. Consulting and Review - Specialised and customised work and business intelligence to improve clients business systems.

Target Market(s)

Target customers are either:
Wholesalers, i.e. companies who own warehouses of inventory and distribute products as wholesalers.
Retailers, i.e. companies operating multiple retail stores and now want to start an online sales program.
Dropship agents, i.e. people who act as brokers, selling products on behalf of wholesalers.
Freight and transport companies who need realtime tracking of products, during delivery from pickup aat warehouse through to delicery at customer.

Industry/Entity Type

Software

Colors

Designer to choose colors to be used in the design.

Requirements
Must have
• A. Simple home page without clutter. Just an easy registration and startup.
minimal menus.
B. Use of icons to indicate each of the 4 areas of work. Namely:
1. Sales - managed sales of products via our existing retail channels or a combination of .our channels and clients channels.
2. Software - use of our platforms, like www.plindar.com , or one of our many webstores. Use of our apps for product management, sales, tracking and customer service notifications
3. Marketing - SEO and strategies to increase sales and broaden exposure.
4. Consulting and Review - Specialised and customised work and business intelligence to improve clients business systems.

C. Registration wizard to on-board a supplier in 3 easy steps, and start selling products. For example list on quilmo in 2 easy steps.

D. Use of HTML5 for graphic interface, moving icons and images for a dynamic experience.

E. Internal app-store to download our own apps.

F. Graphical explanations instead of words.

G. Real images and photos
Should not have
• Many menus.
long winded wordy explanations.

```html
<!DOCTYPE html>
<html lang="en">
<head>
<meta charset="utf-8">
<title>Quorvex — Managed Sales, Software and Apps</title>
<link rel="stylesheet" href="https://fonts.googleapis.com/css2?family=Mulish:wght@300;400;600;900&family=Open+Sans:wght@400;600&display=swap">
<style>
:root{
  --ink:#1c1c1c;
  --text:#3d3d3d;
  --muted:#7a7a7a;
  --pink:#e5327f;
  --green:#8ccc33;
  --orange:#ee9c12;
  --teal:#35d0b0;
  --blue-dark:#1a74bd;
  --panel:#f8f8f8;
  --footer:#000;
  --white:#fff;
}
*{box-sizing:border-box;margin:0;padding:0}
html,body{width:985px;height:1200px;overflow:hidden;background:var(--white)}
body{position:relative;font-family:"Open Sans",Arial,sans-serif;color:var(--text)}

/* header */
.site-header{position:absolute;left:0;top:0;width:985px;height:79px;border-bottom:1px solid #e6e6e6;background:var(--white)}
.brand{position:absolute;left:134px;top:24px;display:flex;align-items:center;gap:8px}
.brand-mark{width:14px;height:14px;background:var(--pink)}
.brand-name{font-family:"Mulish",sans-serif;font-weight:900;font-size:25px;letter-spacing:1px;color:var(--ink)}
.main-nav a{position:absolute;top:34px;font-family:"Mulish",sans-serif;font-size:13px;color:var(--text);text-decoration:none}

/* hero */
.hero{position:absolute;left:0;top:79px;width:985px;height:363px;overflow:hidden;
  background:linear-gradient(90deg,#d9dde2 0%,#eef0f2 30%,#f6f7f8 60%,#e9eaea 100%)}
.hero-photo{position:absolute;left:0;top:0;width:560px;height:363px;
  background:radial-gradient(ellipse at 45% 55%,#a9c4e4 0%,#bcd0e8 35%,rgba(220,226,232,0) 75%)}
.quick-reg{position:absolute;left:624px;top:71px;width:236px;height:234px;background:var(--white);border:1px solid #d6d6d6}
.quick-reg h2{position:absolute;left:24px;top:20px;font-family:"Mulish",sans-serif;font-weight:400;font-size:19px;color:var(--pink)}
.field{position:absolute;left:21px;width:193px;height:24px;border:1px solid #cfcfcf;font-size:8.5px;line-height:12px;color:#666;padding:5px 9px}
.btn-start{position:absolute;left:21px;top:183px;width:96px;height:30px;border-radius:2px;
  background:linear-gradient(#3aa0e3,var(--blue-dark));color:var(--white);font-family:"Mulish",sans-serif;font-size:12px;text-align:center;line-height:30px}
.slider-dots{position:absolute;left:481px;top:341px;display:flex;gap:3px}
.slider-dots span{width:10px;height:10px;border-radius:50%;background:#111}

/* services */
.service{position:absolute;top:471px;width:180px;text-align:center}
.service .badge{width:98px;height:98px;border-radius:50%;margin:0 auto;display:flex;align-items:center;justify-content:center}
.service h3{margin-top:10px;font-family:"Mulish",sans-serif;font-weight:400;font-size:16px;color:#333;white-space:nowrap}
.service p{margin:6px auto 0;font-size:8.6px;line-height:13px;color:var(--muted)}
.partner{position:absolute;display:flex;align-items:center;gap:5px;font-family:"Open Sans",sans-serif;font-weight:600;font-size:12px;color:var(--text)}
.partner-mark{width:12px;height:12px;background:#555}

/* wizard */
.wizard{position:absolute;left:0;top:721px;width:985px;height:267px;background:var(--panel);border-top:1px solid #ececec}
.wizard h2{position:absolute;left:0;width:985px;top:43px;text-align:center;font-family:"Mulish",sans-serif;font-weight:300;font-size:23px;color:#444}
.steps{position:absolute;left:174px;top:96px;width:657px;height:129px;background:var(--white);border:1px solid #e4e4e4;display:flex}
.step{flex:none;text-align:center;border-right:1px solid #e4e4e4;padding-top:20px}
.step:last-child{border-right:none}
.step h3{margin-top:8px;font-family:"Mulish",sans-serif;font-weight:400;font-size:14px;color:var(--pink)}
.step p{margin-top:3px;font-size:8.6px;line-height:13px;color:var(--muted)}

/* footer */
.site-footer{position:absolute;left:0;top:988px;width:985px;height:212px;background:var(--footer);color:var(--white)}
.foot-col{position:absolute;top:33px}
.foot-col h4{font-family:"Mulish",sans-serif;font-weight:400;font-size:15.5px;margin-bottom:8px}
.foot-col a{display:block;color:var(--white);text-decoration:none;font-size:9.5px;line-height:21px}
.social{display:flex;gap:4px;margin-top:4px}
.social span{width:19px;height:19px;border-radius:50%;background:var(--white)}
.copyright{position:absolute;left:156px;top:157px;font-size:9px;color:#ddd}
</style>
</head>
<body>

<header class="site-header">
  <div class="brand"><span class="brand-mark"></span><span class="brand-name">QUORVEX</span></div>
  <nav class="main-nav">
    <a href="#" style="left:496px">Home</a>
    <a href="#" style="left:565px">Reviews</a>
    <a href="#" style="left:646px">About Us</a>
    <a href="#" style="left:732px">Blog</a>
    <a href="#" style="left:793px">Contact</a>
  </nav>
</header>

<section class="hero">
  <div class="hero-photo" role="img" aria-label="Photo of a smiling senior man in a light blue shirt working on a laptop on a sofa"></div>
  <form class="quick-reg">
    <h2>Quick Registration</h2>
    <div class="field" style="top:54px">Your Name</div>
    <div class="field" style="top:85px">Email address</div>
    <div class="field" style="top:116px">Phone no.</div>
    <div class="field" style="top:148px">Location</div>
    <div class="btn-start">Get Started</div>
  </form>
  <div class="slider-dots"><span></span><span></span><span></span><span></span></div>
</section>

<section class="services">
  <div class="service" style="left:139px">
    <div class="badge" style="background:var(--pink)">
      <svg width="56" height="56" viewBox="0 0 56 56" fill="none" stroke="#fff" stroke-width="3">
        <rect x="6" y="36" width="6" height="14" fill="#fff" stroke="none"/>
        <rect x="16" y="30" width="6" height="20" fill="#fff" stroke="none"/>
        <rect x="26" y="24" width="6" height="26" fill="#fff" stroke="none"/>
        <rect x="36" y="18" width="6" height="32" fill="#fff" stroke="none"/>
        <path d="M6 30 L22 18 L30 22 L46 8"/><path d="M38 8 H46 V16"/>
        <text x="14" y="18" fill="#fff" stroke="none" font-family="Mulish,sans-serif" font-weight="900" font-size="17">$</text>
      </svg>
    </div>
    <h3>Sales</h3>
    <p style="width:146px">Managed sales of products via our existing retail channels or a combi-nation of .our channels and clients channels.</p>
  </div>

  <div class="service" style="left:321px">
    <div class="badge" style="background:var(--green)">
      <svg width="56" height="56" viewBox="0 0 56 56" fill="none" stroke="#fff" stroke-width="3">
        <rect x="10" y="8" width="38" height="8" fill="#fff" stroke="none"/>
        <rect x="14" y="16" width="30" height="30"/>
        <circle cx="24" cy="36" r="10" fill="var(--green)"/><circle cx="24" cy="36" r="4"/>
      </svg>
    </div>
    <h3>Software</h3>
    <p style="width:164px">It Use of our platforms, like www.plindar.com , or one of our many webstores. Use of our apps for product management, sales, tracking and cus-tomer service notifications</p>
  </div>

  <div class="service" style="left:493px">
    <div class="badge" style="background:var(--orange)">
      <svg width="64" height="50" viewBox="0 0 64 50" fill="#fff">
        <circle cx="16" cy="16" r="7"/><path d="M4 40 Q4 26 16 26 Q28 26 28 40Z"/>
        <circle cx="48" cy="16" r="7"/><path d="M36 40 Q36 26 48 26 Q60 26 60 40Z"/>
        <circle cx="32" cy="13" r="8"/><path d="M18 42 Q18 24 32 24 Q46 24 46 42Z"/>
      </svg>
    </div>
    <h3>Marketing</h3>
    <p style="width:154px">SEO and strategies to increase sales and broaden exposure.</p>
  </div>
  <div class="partner" style="left:548px;top:650px"><span class="partner-mark"></span>plindar</div>

  <div class="service" style="left:683px">
    <div class="badge" style="background:var(--teal)">
      <svg width="60" height="52" viewBox="0 0 60 52" fill="none" stroke="#fff" stroke-width="3">
        <path d="M8 8 H36 Q40 8 40 12 V26 Q40 30 36 30 H18 L10 37 V30 H8 Q4 30 4 26 V12 Q4 8 8 8Z"/>
        <path d="M22 16 H50 Q56 16 56 22 V36 Q56 42 50 42 H48 V48 L41 42 H28 Q22 42 22 36Z" fill="var(--teal)"/>
        <circle cx="32" cy="29" r="2.5" fill="#fff"/><circle cx="39" cy="29" r="2.5" fill="#fff"/><circle cx="46" cy="29" r="2.5" fill="#fff"/>
      </svg>
    </div>
    <h3>Consulting and Review</h3>
    <p style="width:154px">Specialised and customised work and business intelligence to improve clients business systems.</p>
  </div>
  <div class="partner" style="left:736px;top:666px"><span class="partner-mark"></span>vornibuy</div>
</section>

<section class="wizard">
  <h2>Registration Wizard</h2>
  <div class="steps">
    <div class="step" style="width:224px">
      <svg width="32" height="34" viewBox="0 0 32 34" fill="none" stroke="var(--pink)" stroke-width="2">
        <rect x="2" y="2" width="28" height="30"/>
        <path d="M8 10h2M14 10h12M8 17h2M14 17h12M8 24h2M14 24h12"/>
      </svg>
      <h3>Enter You Details</h3>
      <p>liquam vehicula mi at mauris Maece-<br>nas placerat nisl at consequat</p>
    </div>
    <div class="step" style="width:209px">
      <svg width="34" height="34" viewBox="0 0 34 34">
        <g fill="var(--pink)">
          <circle cx="17" cy="17" r="11"/>
          <rect x="14" y="1" width="6" height="8"/><rect x="14" y="25" width="6" height="8"/>
          <rect x="1" y="14" width="8" height="6"/><rect x="25" y="14" width="8" height="6"/>
          <rect x="14" y="1" width="6" height="8" transform="rotate(45 17 17)"/><rect x="14" y="25" width="6" height="8" transform="rotate(45 17 17)"/>
          <rect x="1" y="14" width="8" height="6" transform="rotate(45 17 17)"/><rect x="25" y="14" width="8" height="6" transform="rotate(45 17 17)"/>
        </g>
        <circle cx="17" cy="17" r="5" fill="#fff"/>
      </svg>
      <h3>Choose Your Service</h3>
      <p>liquam vehicula mi at mauris Maece-<br>nas placerat nisl at consequat</p>
    </div>
    <div class="step" style="width:222px">
      <svg width="48" height="34" viewBox="0 0 48 34" fill="var(--pink)">
        <path d="M2 30 Q10 12 30 12 V4 L46 17 L30 30 V21 Q14 20 2 30Z"/>
      </svg>
      <h3>Get Started Now</h3>
      <p>liquam vehicula mi at mauris Maece-<br>nas placerat nisl at consequat</p>
    </div>
  </div>
</section>

<footer class="site-footer">
  <div class="foot-col" style="left:164px">
    <h4>Get Connected</h4>
    <div class="social" aria-label="Social network links"><span></span><span></span><span></span><span></span></div>
  </div>
  <div class="foot-col" style="left:324px">
    <h4>Who we are</h4>
    <a href="#">About Us</a><a href="#">How it Works</a><a href="#">Blog</a>
  </div>
  <div class="foot-col" style="left:452px">
    <h4>Sublinks</h4>
    <a href="#">Duis tincidunt</a><a href="#">Lectus quis</a><a href="#">Dui viverra vestibulum</a>
  </div>
  <div class="foot-col" style="left:598px">
    <h4>Support</h4>
    <a href="#">Suspendisse</a><a href="#">Culputate aliquam</a><a href="#">Nulla elementum</a><a href="#">Aliquam vehicula</a>
  </div>
  <div class="copyright">© 2014 Company Name &nbsp;All right reserved &nbsp;Term of Use</div>
</footer>

</body>
</html>
```